RP-Steuerberatung WordPress Site fully implemented (tax advisor)

Hello!
I need a little Wordpress Site for my newly founded Tax-Advisor Company.
I am a one-man Office advising in the area of Crypto-Currency.
PLEASE only provide a Design, if you can also Implement a WP-Site afterwards on an existing Webspace.

Please find the Content and Website-Description in the attached Document

Language for the Website is German (for now)

Target Market(s)

Tax-Advisory (specialized in Crypto Currency)

Coding

Coded - Design and coding required

Number of Pages Required

5+ page

Font styles to use
Sans Serif

Requirements
Must have
• Wordpress Implementation afterwards - Details according to attached Project Information Document

```html
<!DOCTYPE html>
<html lang="de">
<head>
<meta charset="utf-8">
<title>RP-Steuerberatung</title>
<link rel="stylesheet" href="https://fonts.googleapis.com/css2?family=Montserrat:wght@800&family=Poppins:ital,wght@0,400;0,500;0,600;1,400&display=swap">
<style>
  :root {
    --bg: #13203a;
    --white: #ffffff;
    --accent-blue: #5b8bd8;
    --orange: #fd8c04;
    --line: #2a3752;
    --photo-a: #2f4f82;
    --photo-b: #b9b4ab;
  }
  * { box-sizing: border-box; margin: 0; padding: 0; }
  html, body { width: 1200px; height: 738px; overflow: hidden; background: var(--bg); }
  body { font-family: "Poppins", sans-serif; color: var(--white); position: relative; }
  .page {
    position: relative; width: 1200px; height: 738px; overflow: hidden;
    background: radial-gradient(circle at 640px 210px, #1a2946 0, transparent 190px),
                radial-gradient(circle at 900px 560px, #182743 0, transparent 230px),
                var(--bg);
  }
  .brand { position: absolute; left: 74px; top: 55px; display: flex; align-items: center; gap: 10px; }
  .brand-mark { width: 44px; height: 44px; background: var(--white); }
  .brand-name { font-weight: 600; font-size: 19px; letter-spacing: 0.6px; }
  .nav { position: absolute; top: 73px; right: 67px; display: flex; gap: 20px; }
  .nav a { color: var(--white); text-decoration: none; font-size: 13px; font-weight: 500; letter-spacing: 0.2px; padding: 0 7px 9px; }
  .nav a.active { color: var(--accent-blue); border-bottom: 1px solid var(--accent-blue); }
  .nav .caret { font-size: 8px; margin-left: 5px; vertical-align: 1px; }
  .hero { position: absolute; left: 75px; top: 278px; }
  .hero h1 { font-family: "Montserrat", sans-serif; font-weight: 800; font-size: 45px; line-height: 48px; letter-spacing: -0.2px; }
  .hero h1 .highlight { color: var(--accent-blue); display: block; }
  .hero p { margin-top: 16px; font-size: 16.5px; line-height: 28px; letter-spacing: 0.3px; }
  .cta {
    display: inline-flex; align-items: center; gap: 8px; margin-top: 17px;
    height: 46px; padding: 0 22px; border-radius: 23px; background: var(--orange);
    color: var(--white); font-size: 15px; font-weight: 600; text-decoration: none;
  }
  .quote { position: absolute; left: 75px; top: 607px; font-style: italic; font-size: 13px; line-height: 22.5px; letter-spacing: 0.3px; }
  .quote-controls { position: absolute; left: 486px; top: 612px; display: flex; flex-direction: column; gap: 5px; }
  .portrait {
    position: absolute; left: 701px; top: 138px; width: 425px; height: 496px;
    background: linear-gradient(135deg, var(--photo-b) 0%, var(--photo-a) 50%, var(--photo-b) 100%);
    opacity: 0.85;
  }
  .footer-line { position: absolute; left: 0; right: 0; top: 678px; border-top: 1px solid var(--line); }
  .copyright { position: absolute; left: 74px; top: 700px; font-size: 12px; letter-spacing: 0.2px; }
  .social { position: absolute; right: 76px; top: 700px; display: flex; gap: 22px; }
  .social span { width: 18px; height: 18px; border-radius: 50%; background: var(--white); display: block; }
</style>
</head>
<body>
<div class="page">
  <div class="brand">
    <span class="brand-mark"></span>
    <span class="brand-name">RP STEUERBERATUNG</span>
  </div>

  <nav class="nav">
    <a href="#" class="active">HOME</a>
    <a href="#">LEISTUNGEN<span class="caret">&#9660;</span></a>
    <a href="#">ÜBER MICH</a>
    <a href="#">KONTAKT</a>
    <a href="#">IMPRESSUM</a>
  </nav>

  <section class="hero">
    <h1>WILLKOMMEN BEI<span class="highlight">RP-STEUERBERATUNG!</span></h1>
    <p>Ihrem Spezialisten bei allen steuerlichen Themen rund um<br>Einkünfte &amp; Vermögen aus Krypto-Assets.</p>
    <a href="#" class="cta">Weiter zu unseren Leistungen
      <svg width="16" height="16" viewBox="0 0 16 16" aria-hidden="true">
        <circle cx="8" cy="8" r="8" fill="#fff"/>
        <path d="M6.5 4.5 10 8l-3.5 3.5" stroke="#fd8c04" stroke-width="2.2" fill="none" stroke-linecap="round" stroke-linejoin="round"/>
      </svg>
    </a>
  </section>

  <blockquote class="quote">“&nbsp; Dann mach ich eine Schweizer<br>Holding-Gesellschaft– dort zahlt man fast keine Steuern..”</blockquote>
  <div class="quote-controls">
    <svg width="14" height="16" viewBox="0 0 14 16" aria-label="Zurück"><path d="M10 1 3 8l7 7" stroke="#fff" stroke-width="1.6" fill="none"/></svg>
    <svg width="14" height="16" viewBox="0 0 14 16" aria-label="Weiter"><path d="M4 1l7 7-7 7" stroke="#fff" stroke-width="1.6" fill="none"/></svg>
  </div>

  <div class="portrait" role="img" aria-label="Foto des Steuerberaters am Schreibtisch mit Brille und blauem Hemd"></div>

  <div class="footer-line"></div>
  <p class="copyright">Copyright ©2022 RP-Steuerberatung All Right Reserved</p>
  <div class="social" aria-label="Soziale Netzwerke">
    <span></span><span></span><span></span><span></span>
  </div>
</div>
</body>
</html>
```